Therapy Services & Training

I provide counseling/therapy to individuals and families. I also travel the country and provide training at conferences.
I would like to see a card which takes my company name and design a logo using the letters "HWAE".
Target Market(s)
Therapists, non-profit organizations, clients looking for therapy
Industry/Entity Type
Training
Contact Information for Business Card
Harborview Wellness Advising & Education LLC
Delia Marsh, M.S.W., LCSW
Clinical Therapist & Trainer
Providing clinical therapy services to individuals, families, couples & children. We also provide life coaching and crisis training.
counselordelia@mailbrook.net
www.harborviewwellnessadvising.com
(555) 214-3092
Millbrook, IL 60999
(BACK SIDE OF CARD)
We are certified by the Ongoing Professional Lawyer Studies (OPLS) Council of the Prairie High Tribunal to provide Continuing Legal Education (CLE) credits to Illinois attorneys. Call about what courses we offer! (555) 214-3092

```html
<!DOCTYPE html>
<html lang="en">
<head>
<meta charset="utf-8">
<title>Harborview Wellness Advising &amp; Education – Business Card</title>
<link href="https://fonts.googleapis.com/css2?family=Jura:wght@400;500;600;700&display=swap" rel="stylesheet">
<style>
  :root {
    --brand-red: #c8161d;
    --brand-red-light: #e8373c;
    --ink: #2a2a2a;
    --ink-soft: #4a4a4a;
    --card: #ffffff;
    --card-edge: #f1f1f1;
    --backdrop: #e7e4df;
  }
  * { box-sizing: border-box; margin: 0; padding: 0; }
  html, body {
    width: 755px; height: 1200px; overflow: hidden;
    background: var(--backdrop);
    font-family: "Jura", sans-serif;
    color: var(--ink);
  }
  .card {
    position: absolute;
    left: 58px;
    width: 640px; height: 366px;
    background: linear-gradient(135deg, var(--card) 55%, var(--card-edge));
    box-shadow: 0 6px 18px rgba(0,0,0,.18);
  }
  .card--front { top: 190px; }
  .card--back  { top: 660px; }

  .edge-tab {
    position: absolute;
    width: 22px; height: 78px;
    background: linear-gradient(90deg, var(--brand-red), var(--brand-red-light));
    border-radius: 5px;
  }
  .edge-tab--left  { left: -6px;  top: 176px; }
  .edge-tab--right { right: -6px; top: 62px; }

  .brand {
    position: absolute; left: 60px; top: 128px; width: 250px;
    text-align: center;
  }
  .brand__mark {
    display: flex; align-items: center; justify-content: center; gap: 10px;
    color: var(--brand-red);
    font-size: 54px; font-weight: 700; letter-spacing: 2px; line-height: 1;
  }
  .brand__dot { width: 22px; height: 22px; border-radius: 50%; background: var(--brand-red); }
  .brand__name {
    margin-top: 10px;
    font-size: 13px; font-weight: 600; line-height: 1.25; color: var(--ink);
  }

  .details {
    position: absolute; left: 348px; top: 58px; width: 270px;
    padding-left: 20px;
    border-left: 2px solid var(--brand-red);
  }
  .details__name { color: var(--brand-red); font-size: 17px; font-weight: 600; }
  .details__cred { font-size: 11px; font-weight: 600; margin-top: 2px; }
  .details__about { font-size: 10px; font-weight: 600; line-height: 1.35; margin-top: 14px; color: var(--ink-soft); }
  .contact { list-style: none; margin-top: 18px; }
  .contact li {
    display: flex; align-items: center; gap: 10px;
    font-size: 11.5px; font-weight: 600; margin-bottom: 6px;
  }
  .contact li:first-child { font-size: 13px; }
  .contact svg { width: 12px; height: 12px; flex: none; fill: var(--brand-red); }

  .back__statement {
    position: absolute; left: 40px; top: 70px; width: 560px;
    font-size: 16px; font-weight: 600; line-height: 2;
  }
  .back__call {
    position: absolute; left: 60px; top: 262px;
    font-size: 19px; font-weight: 600;
  }
  .back__phone {
    display: block; color: var(--brand-red);
    font-size: 25px; font-weight: 700; letter-spacing: 1px;
  }
</style>
</head>
<body>

<section class="card card--front" aria-label="Card front">
  <span class="edge-tab edge-tab--left"></span>
  <span class="edge-tab edge-tab--right"></span>

  <div class="brand">
    <div class="brand__mark"><span class="brand__dot"></span>HWAE</div>
    <p class="brand__name">Harborview Wellness Advising<br>&amp;<br>Education LLC</p>
  </div>

  <div class="details">
    <h1 class="details__name">Delia Marsh</h1>
    <p class="details__cred">M.S.W.</p>
    <p class="details__about">LCSW Clinical Therapist &amp; Trainer Providing clinical therapy services to individuals, families, couples &amp; children. We also provide life coaching and crisis training.</p>
    <ul class="contact">
      <li><svg viewBox="0 0 12 12"><path d="M6 0a4 4 0 0 0-4 4c0 3 4 8 4 8s4-5 4-8a4 4 0 0 0-4-4zm0 5.6A1.6 1.6 0 1 1 6 2.4a1.6 1.6 0 0 1 0 3.2z"/></svg>Millbrook, IL 60999</li>
      <li><svg viewBox="0 0 12 12"><path d="M2.4 0.6l2 2.2-1.1 1.4c.8 1.7 2.1 3 3.8 3.8l1.4-1.1 2.2 2-1.2 1.9C5 10.6 1.4 7 .5 1.8z"/></svg>(555) 214-3092</li>
      <li><svg viewBox="0 0 12 12"><path d="M0 2h12v8H0z"/><path d="M0 2l6 4 6-4" fill="none" stroke="#fff" stroke-width="1"/></svg>counselordelia@mailbrook.net</li>
      <li><svg viewBox="0 0 12 12"><circle cx="6" cy="6" r="5.5"/><path d="M.5 6h11M6 .5v11M2 3h8M2 9h8" stroke="#fff" stroke-width=".7" fill="none"/><ellipse cx="6" cy="6" rx="2.4" ry="5.5" fill="none" stroke="#fff" stroke-width=".7"/></svg>www.harborviewwellnessadvising.com</li>
    </ul>
  </div>
</section>

<section class="card card--back" aria-label="Card back">
  <p class="back__statement">We are certified by the Ongoing Professional Lawyer Studies (OPLS) Council of the Prairie High Tribunal to provide Continuing Legal Education (CLE) credits to Illinois attorneys.</p>
  <p class="back__call">Call about what courses we offer!<span class="back__phone">(555) 214-3092</span></p>
</section>

</body>
</html>
```